Dental Consulting Business Card - Stationary
Business Card / Stationary
Modern
Glen R. Castellano
President
4817 W. Harborview Ave.
Fort Lauderdale, FL
glen@zuvadentalconsulting.example
www.zuvadentalconsulting.example

```html
<!DOCTYPE html>
<html lang="en">
<head>
<meta charset="UTF-8">
<title>ZuvaDental Business Card</title>
<link rel="stylesheet" href="https://fonts.googleapis.com/css2?family=Open+Sans:ital,wght@0,400;0,600;0,700;1,400;1,700&display=swap">
<style>
  :root {
    --page-bg: #e9ebee;
    --card-white: #ffffff;
    --brand-blue: #1f86c8;
    --accent-green: #3dae4a;
    --text-grey: #6b6f73;
    --logo-navy: #2b3a4a;
    --contact-white: #ffffff;
  }
  * { box-sizing: border-box; margin: 0; padding: 0; }
  html, body {
    width: 1200px;
    height: 914px;
    overflow: hidden;
    background: var(--page-bg);
    font-family: "Open Sans", sans-serif;
  }
  .business-card {
    position: absolute;
    left: 100px;
    top: 171px;
    width: 1000px;
    height: 572px;
    background: var(--card-white);
    border-radius: 6px;
    overflow: hidden;
    box-shadow: 0 10px 30px rgba(0,0,0,0.15);
  }
  .card-waves {
    position: absolute;
    inset: 0;
    width: 100%;
    height: 100%;
  }
  .brand-logo {
    position: absolute;
    left: 150px;
    top: 46px;
    display: flex;
    align-items: center;
    gap: 14px;
  }
  .brand-mark {
    width: 34px;
    height: 34px;
    border-radius: 50%;
    background: var(--brand-blue);
  }
  .brand-name {
    font-weight: 700;
    font-size: 46px;
    color: var(--logo-navy);
    letter-spacing: -0.5px;
  }
  .holder {
    position: absolute;
    left: 60px;
    top: 222px;
  }
  .holder-name {
    font-weight: 700;
    font-style: italic;
    font-size: 26px;
    color: var(--brand-blue);
  }
  .holder-title {
    font-style: italic;
    font-size: 20px;
    color: var(--text-grey);
    margin-top: 2px;
  }
  .contact-list {
    position: absolute;
    left: 610px;
    top: 408px;
    list-style: none;
    color: var(--contact-white);
    font-size: 19px;
    line-height: 1.25;
  }
  .contact-item {
    display: flex;
    align-items: flex-start;
    gap: 10px;
    margin-bottom: 4px;
  }
  .contact-icon {
    flex: 0 0 20px;
    width: 20px;
    height: 20px;
    margin-top: 2px;
  }
  .contact-text span { display: block; }
</style>
</head>
<body>
  <div class="business-card">
    <svg class="card-waves" viewBox="0 0 1000 572" preserveAspectRatio="none" aria-hidden="true">
      <path d="M0,340 C200,350 330,400 450,395 C650,390 850,300 1000,205 L1000,572 L0,572 Z" fill="var(--brand-blue)"/>
      <path d="M0,322 C200,332 330,382 450,377 C650,372 850,282 1000,187" fill="none" stroke="var(--accent-green)" stroke-width="6"/>
    </svg>

    <div class="brand-logo">
      <div class="brand-mark"></div>
      <div class="brand-name">ZuvaDental</div>
    </div>

    <div class="holder">
      <div class="holder-name">Glen R. Castellano</div>
      <div class="holder-title">President</div>
    </div>

    <ul class="contact-list">
      <li class="contact-item">
        <svg class="contact-icon" viewBox="0 0 20 20"><circle cx="10" cy="10" r="10" fill="#fff"/><path d="M5 10.5 L10 6 L15 10.5 M7 10 V14 H13 V10" fill="none" stroke="var(--brand-blue)" stroke-width="1.6"/></svg>
        <div class="contact-text"><span>4817 W. Harborview Ave.</span><span>Fort Lauderdale, FL</span></div>
      </li>
      <li class="contact-item">
        <svg class="contact-icon" viewBox="0 0 20 20"><circle cx="10" cy="10" r="10" fill="#fff"/><path d="M7 5 L9 7 L8 9 Q9 11 11 12 L13 11 L15 13 L13.5 15 Q8 14.5 5.5 7 Z" fill="var(--brand-blue)"/></svg>
        <div class="contact-text">(786) 555-0142</div>
      </li>
      <li class="contact-item">
        <svg class="contact-icon" viewBox="0 0 20 20"><circle cx="10" cy="10" r="10" fill="#fff"/><rect x="5" y="6.5" width="10" height="7" fill="none" stroke="var(--brand-blue)" stroke-width="1.4"/><path d="M5 6.5 L10 10.5 L15 6.5" fill="none" stroke="var(--brand-blue)" stroke-width="1.4"/></svg>
        <div class="contact-text">glen@zuvadentalconsulting.example</div>
      </li>
      <li class="contact-item">
        <svg class="contact-icon" viewBox="0 0 20 20"><circle cx="10" cy="10" r="10" fill="#fff"/><circle cx="10" cy="10" r="5" fill="none" stroke="var(--brand-blue)" stroke-width="1.3"/><path d="M5 10 H15 M10 5 Q7 10 10 15 Q13 10 10 5" fill="none" stroke="var(--brand-blue)" stroke-width="1.1"/></svg>
        <div class="contact-text">www.zuvadentalconsulting.example</div>
      </li>
    </ul>
  </div>
</body>
</html>
```